Business Card and Stationary
BrookLamp Consutling
Professional
Peter Varsiklo
8276 Wimbrell Lane
Dublin, OH 43092
pvarsiklo@brooklampconsulting.com
brooklampconsulting.com

```html
<!DOCTYPE html>
<html lang="en">
<head>
<meta charset="utf-8">
<title>BrookLamp Consutling – Business Card</title>
<link href="https://fonts.googleapis.com/css2?family=Arimo:wght@400;600&display=swap" rel="stylesheet">
<style>
  :root {
    --backdrop: #e4e2df;
    --card-front: #ffffff;
    --card-front-shade: #f1f1f1;
    --card-back: #101010;
    --ink: #4a4a4a;
    --ink-soft: #5c5c5c;
    --accent: #7dc142;
    --mark-tile: #d9d9d9;
    --reverse-ink: #f2f2f2;
  }
  html, body {
    margin: 0;
    padding: 0;
    overflow: hidden;
  }
  body {
    width: 1200px;
    height: 838px;
    background: var(--backdrop);
    position: relative;
    font-family: "Arimo", Arial, sans-serif;
  }
  .card {
    position: absolute;
    width: 631px;
    height: 331px;
    border-radius: 24px;
    box-shadow: 0 6px 18px rgba(0,0,0,0.18);
    overflow: hidden;
  }
  .card--front {
    left: 149px;
    top: 96px;
    background: linear-gradient(135deg, var(--card-front) 0%, var(--card-front-shade) 100%);
  }
  .card--back {
    left: 473px;
    top: 403px;
    background: var(--card-back);
  }
  .brand-tile {
    position: absolute;
    left: 43px;
    top: 36px;
    width: 96px;
    height: 96px;
    background: var(--mark-tile);
  }
  .brand-name {
    position: absolute;
    left: 187px;
    top: 52px;
    margin: 0;
    color: var(--ink);
    font-weight: 600;
    line-height: 1;
  }
  .brand-name__main {
    display: block;
    font-size: 36px;
  }
  .brand-name__sub {
    display: block;
    margin-top: 8px;
    font-size: 17px;
    letter-spacing: 5px;
  }
  .holder {
    position: absolute;
    left: 367px;
    top: 190px;
    display: flex;
    align-items: center;
    gap: 14px;
  }
  .holder__name {
    color: var(--accent);
    font-size: 23px;
    font-weight: 600;
  }
  .holder__marker {
    width: 20px;
    height: 20px;
    background: var(--accent);
  }
  .contact {
    position: absolute;
    left: 43px;
    top: 184px;
    margin: 0;
    font-style: normal;
    color: var(--ink-soft);
    font-size: 13px;
    line-height: 18px;
  }
  .contact__group { margin: 0 0 18px; }
  .contact__group:last-child { margin: 0; }
  .back-brand {
    position: absolute;
    left: 0;
    right: 0;
    top: 96px;
    text-align: center;
    color: var(--reverse-ink);
    font-weight: 600;
    font-size: 30px;
    margin: 0;
  }
  .back-site {
    position: absolute;
    left: 0;
    right: 0;
    top: 226px;
    text-align: center;
    color: var(--reverse-ink);
    font-size: 26px;
    margin: 0;
  }
</style>
</head>
<body>
  <section class="card card--front" aria-label="Card front">
    <div class="brand-tile"></div>
    <h1 class="brand-name">
      <span class="brand-name__main">BrookLamp</span>
      <span class="brand-name__sub">Consutling</span>
    </h1>
    <div class="holder">
      <span class="holder__name">Peter Varsiklo</span>
      <span class="holder__marker"></span>
    </div>
    <address class="contact">
      <p class="contact__group">8276 Wimbrell Lane<br>Dublin, OH 43092</p>
      <p class="contact__group">Phone: 614-555-0172<br>pvarsiklo@brooklampconsulting.com</p>
      <p class="contact__group">www.brooklampconsulting.com</p>
    </address>
  </section>

  <section class="card card--back" aria-label="Card back">
    <p class="back-brand">BrookLamp Consutling</p>
    <p class="back-site">www.brooklampconsulting.com</p>
  </section>
</body>
</html>
```